Medicaid and Nursing Home Planning Law Firm Needs Customizable Flyer

We need a flyer for The Delvecki Law Firm, P.C. that incorporates our logo, color scheme and existing collaterals (see uploads) and that can be easily updated. The flyer could advertise an upcoming speech/seminar/gathering, but the text should be customizable so that we can revise it later on using either MSWord or some other basic software.

Industry/Entity Type

Legal

Requirements
Must have
• Logo and contact information for business, including address, phone number, email and website information
Nice to have
• Also should advertise our 2nd location: 418 Brantley Avenue, Suite 305, Watertown, NY 13688

```html
<!DOCTYPE html>
<html lang="en">
<head>
<meta charset="utf-8">
<title>The Delvecki Law Firm – Flyer</title>
<link href="https://fonts.googleapis.com/css2?family=Open+Sans:wght@400;600;700&family=Cinzel:wght@700&display=swap" rel="stylesheet">
<style>
  :root{
    --canvas:#e8e5e1;
    --paper:#ffffff;
    --orange:#d9772a;
    --orange-text:#e07b28;
    --band:#4b4b4b;
    --ink:#4f4f4f;
    --footer:#e4e4e4;
    --white:#ffffff;
  }
  *{box-sizing:border-box;margin:0;padding:0}
  html,body{width:887px;height:1200px;overflow:hidden;background:var(--canvas)}
  body{font-family:"Open Sans",Arial,sans-serif;color:var(--ink);position:relative}

  .flyer{position:absolute;left:43px;top:32px;width:800px;height:1134px;background:var(--paper);box-shadow:0 6px 22px rgba(0,0,0,.18);overflow:hidden}

  /* header */
  .masthead{position:absolute;left:0;top:0;width:800px;height:220px;background:var(--paper)}
  .brand{position:absolute;left:36px;top:92px;display:flex;align-items:center;gap:12px}
  .brand-mark{width:22px;height:22px;background:var(--ink)}
  .brand-name{font-size:26px;font-weight:400;letter-spacing:.5px;color:var(--ink);text-transform:uppercase}
  .masthead-divider{position:absolute;left:449px;top:46px;width:1px;height:140px;background:#bdbdbd}
  .contact{position:absolute;left:478px;top:40px;font-size:15px;line-height:20px;color:var(--ink)}
  .contact .label{color:var(--orange-text);font-weight:700}
  .contact .strong{font-weight:600}
  .contact .gap{margin-top:9px}
  .contact .gap-lg{margin-top:21px}

  .band{position:absolute;left:0;width:800px;height:9px;background:var(--band)}
  .band.top{top:220px}
  .band.mid{top:699px}

  /* hero */
  .hero{position:absolute;left:0;top:229px;width:800px;height:470px}
  .hero-photo{position:absolute;inset:0;background:
    radial-gradient(ellipse at 22% 45%, #ffd37a 0%, #f0a646 18%, rgba(196,112,48,.6) 42%, rgba(120,70,40,0) 70%),
    linear-gradient(180deg,#e8d9c6 0%,#d9b48a 30%,#b97a45 55%,#8a5634 80%,#6e4a33 100%)}
  .hero-headline{position:absolute;left:39px;top:36px;font-size:30px;line-height:40px;font-weight:400;color:#2e2e2e;text-transform:uppercase}
  .hero-services{position:absolute;left:39px;top:262px;font-size:20px;line-height:29px;font-weight:700;color:var(--white);width:336px}

  /* orange panel */
  .info{position:absolute;left:0;top:708px;width:800px;height:331px;background:var(--orange);color:var(--white)}
  .about{position:absolute;left:39px;top:16px;width:282px}
  .about h2{font-size:30px;font-weight:400;line-height:40px}
  .about p{margin-top:10px;font-size:14.5px;line-height:20px}
  .info-divider{position:absolute;left:340px;top:24px;width:1px;height:190px;background:rgba(255,255,255,.45)}
  .services{position:absolute;left:365px;top:18px}
  .services h2{font-size:27px;font-weight:600;line-height:36px}
  .services ul{list-style:none;margin-top:12px}
  .services li{display:flex;align-items:center;gap:11px;font-size:17.5px;font-weight:700;line-height:28px}
  .services svg{flex:none}
  .call{position:absolute;left:0;top:272px;width:800px;text-align:center;font-family:"Cinzel",Georgia,serif;font-size:40px;font-weight:700;letter-spacing:.5px;text-shadow:0 2px 3px rgba(0,0,0,.3)}

  /* footer */
  .footer{position:absolute;left:0;top:1039px;width:800px;height:95px;background:var(--footer)}
  .social{position:absolute;left:39px;top:26px;font-size:16px;line-height:21px;color:var(--ink)}
  .social li{list-style:none;display:flex;align-items:center;gap:8px}
  .social .dot{width:12px;height:12px;background:var(--orange)}
  .cta{position:absolute;right:38px;top:16px;text-align:center}
  .cta .book{font-size:21.5px;line-height:28px;color:var(--ink)}
  .cta .url{font-size:23px;line-height:32px;color:var(--orange-text)}
</style>
</head>
<body>
<main class="flyer">
  <header class="masthead">
    <div class="brand">
      <span class="brand-mark"></span>
      <span class="brand-name">The Delvecki Law Firm</span>
    </div>
    <div class="masthead-divider"></div>
    <div class="contact">
      <div>2740 Fairmount Parkway</div>
      <div>East Syracuse, New York</div>
      <div class="gap"><span class="label">3057 Office:</span> <span class="strong">(315) 555-0147</span></div>
      <div><span class="label">Email:</span> <span class="strong">info@thedelveckilawfirm.com</span></div>
      <div class="gap-lg"><span class="label">2nd location:</span> 418 Brantley Avenue,</div>
      <div>Suite 305, Watertown, NY 13688</div>
    </div>
  </header>

  <div class="band top"></div>

  <section class="hero">
    <div class="hero-photo" role="img" aria-label="Photo of an older couple seen from behind, arms around each other, in a golden field at sunset"></div>
    <h1 class="hero-headline">Protecting<br>everything that<br>matters to you.</h1>
    <p class="hero-services">New Yours Elder Low, Medicaid, Estate planing, Trust &amp; Estate Litigation, Guardianship<br>and Special Needs planning<br>Low Firm</p>
  </section>

  <div class="band mid"></div>

  <section class="info">
    <div class="about">
      <h2>About US</h2>
      <p>The Delvecki Law Firm, P. C. was founded in 2015 to focus soley on planning for residentsof Central and Northern New York with needs in Elder law/Medicaid Planning, Estate Planning, trust &amp; Estate Administration /Litigation, and Guardianship / Special Needs Planning Areas.</p>
    </div>
    <div class="info-divider"></div>
    <div class="services">
      <h2>Services We Offer</h2>
      <ul>
        <li><svg width="16" height="16" viewBox="0 0 16 16"><circle cx="8" cy="8" r="8" fill="#fff"/><path d="M4.3 8.2l2.5 2.5 4.9-5" fill="none" stroke="#d9772a" stroke-width="2.2" stroke-linecap="round" stroke-linejoin="round"/></svg>Elder Law</li>
        <li><svg width="16" height="16" viewBox="0 0 16 16"><circle cx="8" cy="8" r="8" fill="#fff"/><path d="M4.3 8.2l2.5 2.5 4.9-5" fill="none" stroke="#d9772a" stroke-width="2.2" stroke-linecap="round" stroke-linejoin="round"/></svg>Medicaid Planning</li>
        <li><svg width="16" height="16" viewBox="0 0 16 16"><circle cx="8" cy="8" r="8" fill="#fff"/><path d="M4.3 8.2l2.5 2.5 4.9-5" fill="none" stroke="#d9772a" stroke-width="2.2" stroke-linecap="round" stroke-linejoin="round"/></svg>Estate Planning</li>
        <li><svg width="16" height="16" viewBox="0 0 16 16"><circle cx="8" cy="8" r="8" fill="#fff"/><path d="M4.3 8.2l2.5 2.5 4.9-5" fill="none" stroke="#d9772a" stroke-width="2.2" stroke-linecap="round" stroke-linejoin="round"/></svg>Trust &amp; Estate Administration</li>
        <li><svg width="16" height="16" viewBox="0 0 16 16"><circle cx="8" cy="8" r="8" fill="#fff"/><path d="M4.3 8.2l2.5 2.5 4.9-5" fill="none" stroke="#d9772a" stroke-width="2.2" stroke-linecap="round" stroke-linejoin="round"/></svg>Trust &amp; Estate Litigation</li>
        <li><svg width="16" height="16" viewBox="0 0 16 16"><circle cx="8" cy="8" r="8" fill="#fff"/><path d="M4.3 8.2l2.5 2.5 4.9-5" fill="none" stroke="#d9772a" stroke-width="2.2" stroke-linecap="round" stroke-linejoin="round"/></svg>Guardianship/special Needs Planning Areas</li>
      </ul>
    </div>
    <div class="call">CALL US TODAY : (315) 555-0147</div>
  </section>

  <footer class="footer">
    <ul class="social">
      <li><span class="dot"></span>follow.thedelveckilawfirm.com</li>
      <li><span class="dot"></span>Updates: delveckielderlaw</li>
    </ul>
    <div class="cta">
      <div class="book">BOOK A FREE CONSULTATION NOW!!!</div>
      <div class="url">www.thedelveckilawfirm.com</div>
    </div>
  </footer>
</main>
</body>
</html>
```